BRANWICK SKY FESTIVAL JULY 2017

INVITATION TO MEDICAL LECTURE AT BRANWICK SKYFESTIVAL 2017, JULY 25TH, THIS WILL BE MAILED TO APPROX 750 AVIATION MEDICAL EXAMINERS, MDS.

Target Market(s)

Aviation Medical Examiners

Industry/Entity Type

Medical

Colors
ec1f27
3377b5

Requirements
Must have
• Front of postcard: Art to include Airplane, Medical / Staff of Medicine Icon,
• Back of postcard:
• GO BEYOND STANDARD LIPID TESTING AND IMPROVE CARDIAC RISK:
• BRANWICK SKY FESTIVAL 2017, TUESDAY JULY 25th, LORN THEATRE
• 8:00-9:00 am “CODE BLUE AT 40,000 FEET” DR. MARTIN VOSKETT
• 9:00-10:00 am “VERY HIGH RISK GROUPS WITH CORONARY HEART DISEASE, A NATIONAL EMERGENCY” DR. DANIEL HALVERIN
• 10:00-11:00 am “BEYOND CHOLESTEROL, THE NEED FOR ADVANCED LIPIDS, APPLICATION TO PILOTS” DR. DANIEL HALVERIN
• 11:00-12:00 am “PROTECTING THE COCKPIT, PILOTS AND UNDETECTED HEART DISEASE” DR. WALTER BRISCOM
• 1:00-2:00 am “PERSONAL LIFESTYLE MODIFICATIONS TO DECREASE HEART DISEASE” ADA FENN, NP
• RSVP: Marian Holtzfeld 548-206-917
Nice to have
• ON BACK all info above to list medical presentations, Cardiac Heart Icon, (heart with rhythm logo), on left, address to attendee on the right
• ON FRONT: Color POP with AVIATION THEME
Should not have
• Fancy Font, (please keep it clean and simple, easy to read)

```html
<!DOCTYPE html>
<html lang="en">
<head>
<meta charset="utf-8">
<title>Branwick Sky Festival 2017 – Medical Lecture Invitation</title>
<link rel="stylesheet" href="https://fonts.googleapis.com/css2?family=Source+Sans+3:wght@400;700&display=swap">
<style>
  :root {
    --blue-deep: #2a6fb3;
    --blue-mid: #1a8dcc;
    --blue-light: #12a3dc;
    --red: #ec1f27;
    --white: #ffffff;
    --page: #ffffff;
  }
  * { margin: 0; padding: 0; box-sizing: border-box; }
  html, body {
    width: 1200px; height: 800px; overflow: hidden;
    background: var(--page);
  }
  .canvas {
    position: relative; width: 1200px; height: 800px; overflow: hidden;
    background: var(--page);
    font-family: "Source Sans 3", "Myriad Pro", Arial, sans-serif;
    color: var(--white);
  }
  .postcard-back {
    position: absolute; left: 0; top: 0; width: 598px; height: 800px;
    background: radial-gradient(ellipse 70% 60% at 50% 50%, var(--blue-light) 0%, var(--blue-mid) 50%, var(--blue-deep) 100%);
    text-transform: uppercase;
    text-align: center;
  }
  .headline {
    position: absolute; left: 0; width: 598px; top: 20px;
    font-weight: 700; font-size: 28px; line-height: 24px; letter-spacing: -0.2px;
  }
  .heart-icon {
    position: absolute; left: 46px; top: 80px; width: 96px; height: 80px;
  }
  .event-details {
    position: absolute; left: 170px; width: 382px; top: 97px;
    text-align: right; font-size: 22px; line-height: 22px;
  }
  .event-details .line { display: block; text-align: center; padding-left: 30px; }
  .event-details .line:last-child { padding-left: 0; }
  .session {
    position: absolute; left: 0; width: 598px;
    font-size: 22px; line-height: 24.5px;
  }
  .session .time {
    display: block; font-weight: 700; font-size: 23px; text-transform: lowercase;
  }
  .session .time .num { text-transform: none; }
  .rsvp-band {
    position: absolute; left: 0; top: 678px; width: 598px; height: 87px;
    background: var(--red);
    text-align: center; text-transform: none;
    padding-top: 7px;
  }
  .rsvp-band .label { display: block; font-weight: 700; font-size: 23px; line-height: 24px; }
  .rsvp-band .contact { display: block; font-weight: 700; font-size: 23px; line-height: 24px; }
  .rsvp-band .phone { display: block; font-weight: 400; font-size: 22px; line-height: 24px; }
</style>
</head>
<body>
<main class="canvas">
  <section class="postcard-back">
    <h1 class="headline">Go beyond standard lipid testing<br>and improve cardiac risk:</h1>

    <svg class="heart-icon" viewBox="0 0 96 80" aria-hidden="true">
      <path d="M48 78 C30 62 6 46 6 24 C6 10 17 2 28 2 C37 2 44 7 48 14 C52 7 59 2 68 2 C79 2 90 10 90 24 C90 46 66 62 48 78 Z" fill="var(--red)"/>
      <polyline points="0,38 28,38 32,30 36,44 40,22 44,50 48,32 52,40 56,36 60,38 96,38"
        fill="none" stroke="var(--white)" stroke-width="1.6" stroke-linejoin="round"/>
    </svg>

    <p class="event-details">
      <span class="line">Branwick Sky Festival 2017,</span>
      <span class="line">Tuesday July 25th, Lorn Theatre</span>
    </p>

    <div class="session" style="top:161px">
      <span class="time"><span class="num">8:00-9:00</span> am</span>
      “Code blue at 40,000 feet”<br>Dr. Martin Voskett
    </div>
    <div class="session" style="top:245px">
      <span class="time"><span class="num">9:00-10:00</span> am</span>
      “Very high risk groups with coronary heart<br>disease, a national emergency”<br>Dr. Daniel Halverin
    </div>
    <div class="session" style="top:354px">
      <span class="time"><span class="num">10:00-11:00</span> am</span>
      “Beyond cholesterol, the need for advanced<br>lipids, application to pilots”<br>Dr. Daniel Halverin
    </div>
    <div class="session" style="top:464px">
      <span class="time"><span class="num">11:00-12:00</span> am</span>
      “Protecting the cockpit, pilots and<br>undetected heart disease”<br>Dr. Walter Briscom
    </div>
    <div class="session" style="top:572px">
      <span class="time"><span class="num">1:00-2:00</span> am</span>
      “Personal lifestyle modifications to<br>decrease heart disease”<br>Ada Fenn, NP
    </div>

    <div class="rsvp-band">
      <span class="label">RSVP:</span>
      <span class="contact">Marian Holtzfeld</span>
      <span class="phone">548-206-917</span>
    </div>
  </section>
</main>
</body>
</html>
```